Create modern and sleek business card for luxury real estate company

We're a "boutique" real estate office looking for a design that gets across a highly modern luxury brand. Blacks and whites are probably the best colors unless we try a silver foil for the logo. I've attached a version of our current logo here. I'd like to swap out the current font on there with Gotham Light Regular.

I'm looking to have one side of the card have the logo with the space for our agents info on the other side.

Target Market(s)

Young professionals in a "luxury" headspace

Industry/Entity Type

Real estate

Contact Information for Business Card

A place for agent name, cell number, website. The slogan "Simply Rethinking Real Estate".

Font styles to use
Other font styles liked:
• Gotham Regular

Colors

Designer to choose only greyscale colors for use in the design.

Requirements
Must have
• Matte black as the background color. Clean lines and use of contrast. A specific design aspect that will use silver foil.
Nice to have
• Up in the air on integrating a QR code
Should not have
• Any houses or other real estate related design (ex: a clip art house)

```html
<!DOCTYPE html>
<html lang="en">
<head>
<meta charset="utf-8">
<title>Halden Realty Stationery</title>
<link rel="stylesheet" href="https://fonts.googleapis.com/css2?family=Montserrat:wght@300;400;500&family=Arimo:wght@400;700&display=swap">
<style>
:root{
  --backdrop:#cbc8c9;
  --ink-dark:#333333;
  --paper:#ffffff;
  --on-dark:#ffffff;
  --text:#3a3a3a;
  --text-soft:#8a8a8a;
}
*{margin:0;padding:0;box-sizing:border-box}
html,body{width:1200px;height:900px;overflow:hidden;background:var(--backdrop)}
body{position:relative;font-family:"Montserrat",sans-serif;color:var(--text)}
.sheet{position:absolute;background:var(--paper)}
.band{position:absolute;left:0;right:0;top:0;background:var(--ink-dark)}
.brand{position:absolute;display:flex;align-items:center;color:var(--on-dark)}
.brand-ring{border:1.5px solid var(--on-dark);border-radius:50%;flex:none}
.brand-name{font-family:"Montserrat",sans-serif;font-weight:400;line-height:1.05;text-align:center;letter-spacing:.5px}
.contact{position:absolute;font-family:"Arimo",sans-serif;color:var(--on-dark);font-size:8.5px;line-height:10.5px}
.contact li{list-style:none;display:flex;align-items:center;gap:5px}
.contact svg{width:7px;height:7px;fill:var(--on-dark)}

/* letterhead */
.letterhead{left:51px;top:100px;width:497px;height:703px}
.letterhead .band{height:82px}
.letterhead .brand{left:23px;top:22px;gap:8px}
.letterhead .brand-ring{width:40px;height:40px}
.letterhead .brand-name{font-size:17px}
.letterhead .contact{left:382px;top:15px}
.letter{position:absolute;left:50px;top:156px;width:398px}
.letter-to{font-size:9.5px;letter-spacing:1px}
.letter-date{position:absolute;right:0;top:0;font-size:7.5px}
.recipient-name{font-size:9px;margin-top:4px;font-weight:500}
.recipient-lines{font-size:6.5px;color:var(--text-soft);line-height:10.5px;margin-top:3px}
.letter-body{margin-top:27px;font-size:7.3px;line-height:8.8px;text-align:justify;color:var(--text-soft)}
.letter-body p{margin-bottom:9px}
.signature{width:88px;height:14px;margin-top:39px;background:linear-gradient(90deg,#d9d9d9,#eeeeee);border-radius:2px}
.signer{font-size:8px;margin-top:8px;font-weight:500}
.signer-role{font-size:6.5px;color:var(--text-soft);margin-top:2px}

/* business cards */
.card{position:absolute;top:96px;width:274px;height:156px;background:var(--ink-dark)}
.card-front{left:577px}
.card-back{left:875px}
.card-front .brand{left:22px;top:62px;gap:6px}
.card-front .brand-ring{width:30px;height:30px}
.card-front .brand-name{font-size:13px}
.card-divider{position:absolute;left:137px;top:38px;width:1px;height:82px;background:var(--on-dark)}
.agent{position:absolute;left:149px;top:36px;color:var(--on-dark);font-family:"Arimo",sans-serif}
.agent-name{font-size:11px;font-weight:700}
.agent-role{font-size:7px;margin-top:2px}
.card-front .contact{left:149px;top:64px;font-size:7.5px;line-height:9.5px}
.card-back .brand{left:71px;top:57px;gap:8px}
.card-back .brand-ring{width:40px;height:40px}
.card-back .brand-name{font-size:17px}

/* envelope */
.envelope-front{left:577px;top:282px;width:572px;height:248px}
.envelope-front .band{height:59px}
.envelope-front .brand{left:16px;top:14px;gap:8px}
.envelope-front .brand-ring{width:32px;height:32px}
.envelope-front .brand-name{font-size:14px}
.return-address{position:absolute;left:21px;top:67px;font-family:"Arimo",sans-serif;font-size:8.5px;line-height:10.5px;color:#222}
.envelope-back{left:577px;top:555px;width:572px;height:248px}
.flap{position:absolute;left:0;top:0}
.envelope-back .brand{left:232px;top:16px;gap:7px}
.envelope-back .brand-ring{width:32px;height:32px}
.envelope-back .brand-name{font-size:14px}
</style>
</head>
<body>

<section class="sheet letterhead">
  <div class="band">
    <div class="brand"><span class="brand-ring"></span><span class="brand-name">HALDEN<br>REALTY</span></div>
    <ul class="contact">
      <li>Your address, city</li>
      <li>state, ZIP 0000</li>
      <li><svg viewBox="0 0 10 10"><path d="M2 0h2l1 3-1.5 1a6 6 0 0 0 2.5 2.5L7 5l3 1v2a2 2 0 0 1-2 2A8 8 0 0 1 0 2a2 2 0 0 1 2-2z"/></svg>555-014-2100</li>
      <li><svg viewBox="0 0 10 10"><path d="M0 2h10v6H0zM1 3v.5l4 2.5 4-2.5V3L5 5.5z" fill-rule="evenodd"/></svg>hello@haldenrealty.com</li>
      <li><svg viewBox="0 0 10 10"><circle cx="5" cy="5" r="5"/></svg>www.haldenrealty.com</li>
    </ul>
  </div>
  <article class="letter">
    <div class="letter-to">TO</div>
    <div class="letter-date">Friday, 01/01/2018</div>
    <div class="recipient-name">Clara Whitfield</div>
    <div class="recipient-lines">Human Resources<br>Brightline Co<br>410 Larch Avenue, Westbrook<br>WB 20410 USA</div>
    <div class="letter-body">
      <p>We are pleased to introduce our boutique office and the residences we represent across the city. Our team pairs careful market study with quiet, personal service, so every client receives clear advice at each step. We would welcome the chance to learn about your relocation plans and to show how our approach can serve your staff well.</p>
      <p>Our listings span modern apartments, townhomes and private estates, each selected for design, location and lasting value.</p>
      <p>Thank you for your time and interest.</p>
      <p>Enclosed you will find a short guide to current homes, recent sales in nearby districts and a summary of the services we offer to companies that move employees into the area. Each section is brief and written to help your team compare options quickly.</p>
      <p>Should you have questions, our managing director will gladly arrange a meeting at a time that suits you. We look forward to hearing from you and to building a lasting working relationship with your office.</p>
      <p>With kind regards from all of us at the office.</p>
    </div>
    <div class="signature" role="img" aria-label="Handwritten signature of Paul Mercer"></div>
    <div class="signer">Paul Mercer</div>
    <div class="signer-role">Managing Director</div>
  </article>
</section>

<section class="card card-front">
  <div class="brand"><span class="brand-ring"></span><span class="brand-name">HALDEN<br>REALTY</span></div>
  <div class="card-divider"></div>
  <div class="agent">
    <div class="agent-name">Daniel Reyes</div>
    <div class="agent-role">Manager</div>
  </div>
  <ul class="contact">
    <li>Your address, city</li>
    <li>state, ZIP 0000</li>
    <li style="margin-top:6px"><svg viewBox="0 0 10 10"><path d="M2 0h2l1 3-1.5 1a6 6 0 0 0 2.5 2.5L7 5l3 1v2a2 2 0 0 1-2 2A8 8 0 0 1 0 2a2 2 0 0 1 2-2z"/></svg>555-014-2100</li>
    <li><svg viewBox="0 0 10 10"><path d="M0 2h10v6H0zM1 3v.5l4 2.5 4-2.5V3L5 5.5z" fill-rule="evenodd"/></svg>hello@haldenrealty.com</li>
    <li><svg viewBox="0 0 10 10"><circle cx="5" cy="5" r="5"/></svg>www.haldenrealty.com</li>
  </ul>
</section>

<section class="card card-back">
  <div class="brand"><span class="brand-ring"></span><span class="brand-name">HALDEN<br>REALTY</span></div>
</section>

<section class="sheet envelope-front">
  <div class="band">
    <div class="brand"><span class="brand-ring"></span><span class="brand-name">HALDEN<br>REALTY</span></div>
  </div>
  <div class="return-address">Your address, city<br>state, ZIP 0000</div>
</section>

<section class="sheet envelope-back">
  <svg class="flap" width="572" height="70" viewBox="0 0 572 70">
    <path d="M0 0H572L560 45Q555 68 530 68H42Q17 68 12 45Z" fill="var(--ink-dark)"/>
  </svg>
  <div class="brand"><span class="brand-ring"></span><span class="brand-name">HALDEN<br>REALTY</span></div>
</section>

</body>
</html>
```